Falcrest security business card

Looking for a business card for my security company

Target Market(s)

Security

Industry/Entity Type

Security

Contact Information for Business Card

Name - Gil Marston. Title - General manager - direct 314 862.4490 website www. falcrestsecurityservices.example email - gil@ falcrestsecurityservices.example

Requirements
Must have
• Logo attached

```html
<!DOCTYPE html>
<html lang="en">
<head>
<meta charset="utf-8">
<title>Falcrest Security Services – Business Card</title>
<link href="https://fonts.googleapis.com/css2?family=Arimo:wght@400;700&display=swap" rel="stylesheet">
<style>
  :root {
    --backdrop: #1b1b1b;
    --card-dark: #212121;
    --card-light: #ffffff;
    --ink: #222222;
    --gold: #c39a4e;
    --gold-light: #f3e7b8;
    --text-light: #ffffff;
  }
  * { margin: 0; padding: 0; box-sizing: border-box; }
  html, body {
    width: 1200px;
    height: 1059px;
    overflow: hidden;
    background: var(--backdrop);
    font-family: "Arimo", Arial, sans-serif;
  }
  .card {
    position: absolute;
    width: 690px;
    height: 391px;
    border-radius: 24px;
    overflow: hidden;
  }
  .card-front { left: 256px; top: 89px; background: var(--card-light); }
  .card-back { left: 255px; top: 547px; background: var(--card-dark); }
  .wave { position: absolute; inset: 0; width: 100%; height: 100%; }
  .brand-name {
    position: absolute;
    font-weight: 700;
    letter-spacing: 1px;
    text-transform: uppercase;
    white-space: nowrap;
    transform: translateX(-50%);
  }
  .card-front .brand-name { left: 526px; top: 86px; font-size: 40px; color: var(--ink); }
  .card-back .brand-name { left: 345px; top: 168px; font-size: 58px; color: var(--gold); }
  .holder {
    position: absolute;
    left: 30px;
    top: 230px;
    color: var(--text-light);
  }
  .holder-name { font-size: 23px; font-weight: 700; line-height: 1.1; }
  .holder-title { font-size: 16px; font-weight: 400; margin-top: 2px; }
  .contacts {
    position: absolute;
    left: 30px;
    top: 293px;
    list-style: none;
    color: var(--text-light);
    font-size: 16px;
  }
  .contacts li {
    display: flex;
    align-items: center;
    height: 25px;
  }
  .contacts svg { width: 14px; height: 14px; margin-right: 8px; fill: var(--text-light); }
</style>
</head>
<body>
  <section class="card card-front">
    <svg class="wave" viewBox="0 0 690 391" preserveAspectRatio="none" aria-hidden="true">
      <defs>
        <linearGradient id="goldSweep" x1="0" x2="1" y1="0" y2="0">
          <stop offset="0" stop-color="#9a7432"/>
          <stop offset="0.6" stop-color="#f3e7b8"/>
          <stop offset="1" stop-color="#b8873b"/>
        </linearGradient>
      </defs>
      <path fill="url(#goldSweep)" d="M311,205 C420,243 500,270 560,273 C630,276 672,240 690,192 L690,212 C666,262 620,287 555,286 C490,284 420,256 311,205 Z"/>
      <path fill="var(--card-dark)" d="M0,243 C40,192 100,176 150,179 C230,184 330,224 440,260 C520,287 590,298 640,270 C665,256 680,240 690,220 L690,391 L0,391 Z"/>
    </svg>

    <div class="brand-name">Falcrest</div>

    <div class="holder">
      <div class="holder-name">GIL MARSTON</div>
      <div class="holder-title">General manager</div>
    </div>

    <ul class="contacts">
      <li>
        <svg viewBox="0 0 24 24" aria-hidden="true"><path d="M6.6 10.8a15 15 0 0 0 6.6 6.6l2.2-2.2a1 1 0 0 1 1-.25 11.4 11.4 0 0 0 3.6.57 1 1 0 0 1 1 1V20a1 1 0 0 1-1 1A17 17 0 0 1 3 4a1 1 0 0 1 1-1h3.5a1 1 0 0 1 1 1c0 1.25.2 2.45.57 3.57a1 1 0 0 1-.25 1z"/></svg>
        314 862.4490
      </li>
      <li>
        <svg viewBox="0 0 24 24" aria-hidden="true"><path d="M2 5h20v14H2zM4 7v.3l8 5.4 8-5.4V7zm0 2.7V17h16V9.7l-8 5.4z"/></svg>
        gil@falcrestsecurityservices.example
      </li>
      <li>
        <svg viewBox="0 0 24 24" aria-hidden="true"><path d="M12 2a10 10 0 1 0 0 20 10 10 0 0 0 0-20zm-1 17.9A8 8 0 0 1 4.2 10.6L9 15.4v1a2 2 0 0 0 2 2zm6.9-2.5A2 2 0 0 0 16 16h-1v-3a1 1 0 0 0-1-1H8v-2h2a1 1 0 0 0 1-1V7h2a2 2 0 0 0 2-2v-.4a8 8 0 0 1 2.9 12.8z"/></svg>
        www.falcrestsecurityservices.example
      </li>
    </ul>
  </section>

  <section class="card card-back">
    <div class="brand-name">Falcrest</div>
  </section>
</body>
</html>
```